Business Card Design Project

we are a Disc Jockey service. our slogan is "we do more than just play music" we entertain all types of events from weddings to birthday parties. We do more weddings than other types of events
A 2 sided card is ok by us seeing how there is a lot of info incorperate into the design
I have seen lots of cards with a photo of a bride and groom in the background and we like that concept

Industry/Entity Type

Events

Requirements
Must have
• to use our logo
phone # 415-762-9184
www.brightlanternsound.com

Must be saved as CMYK and no less than 300dpi at actual size. NO RGB FILES ACCEPTED. Images need to be TIF or EPS formats. All images need to be supplied to be linked to layout files. A list of font types need to be included

On Second side of card we need web address
plus the following info

weddings, Anniversaries, Corporate events
Holiday parties, Fund raisers
or any event that needs entertainment

plus a space for some ones name a title we have 4 people so there will be 4 different cards made
Nice to have
• we have seen a few other DJ services use a photo of a bride and groom in the background and like that concept.

```html
<!DOCTYPE html>
<html lang="en">
<head>
<meta charset="utf-8">
<title>Bright Lantern Sound – Business Card</title>
<link rel="stylesheet" href="https://fonts.googleapis.com/css2?family=Arimo:wght@400;700&display=swap">
<style>
  :root {
    --brand-blue: #1c1cc0;
    --brand-green: #3b8c1f;
    --ink-soft: #2b2b6e;
    --page-bg: #ffffff;
    --photo-light: #f3f7f1;
    --photo-mist: #e3ece4;
    --photo-gold: #c9a24a;
    --photo-gold-deep: #9a7426;
  }
  html, body {
    margin: 0;
    padding: 0;
    width: 1200px;
    height: 368px;
    overflow: hidden;
    background: var(--page-bg);
    font-family: "Arimo", Arial, sans-serif;
  }
  .sheet { position: relative; width: 1200px; height: 368px; }
  .card {
    position: absolute;
    top: 0;
    width: 567px;
    height: 368px;
    border-radius: 16px;
    overflow: hidden;
  }
  .card--front { left: 0; }
  .card--back { left: 633px; }
  .card__photo {
    position: absolute;
    inset: 0;
    background:
      radial-gradient(ellipse 150px 170px at 86% 58%, var(--photo-gold) 0%, var(--photo-gold-deep) 45%, rgba(201,162,74,0.25) 70%, transparent 80%),
      radial-gradient(ellipse 110px 120px at 70% 48%, rgba(201,162,74,0.7) 0%, rgba(201,162,74,0) 75%),
      linear-gradient(160deg, var(--photo-light) 0%, var(--photo-mist) 55%, #eef2ea 100%);
  }
  .card p, .card h1, .card ul { margin: 0; }
  .brand {
    position: absolute;
    color: var(--brand-blue);
    font-weight: 700;
    line-height: 1;
    display: flex;
    align-items: center;
    gap: 8px;
    white-space: nowrap;
  }
  .brand__dot {
    width: 14px;
    height: 14px;
    border-radius: 50%;
    background: var(--brand-green);
    flex: none;
  }
  .brand--large { left: 12px; top: 96px; font-size: 32px; }
  .brand--small { left: 16px; top: 296px; font-size: 19px; gap: 6px; }
  .brand--small .brand__dot { width: 10px; height: 10px; }
  .slogan-small {
    position: absolute;
    left: 12px;
    top: 158px;
    font-size: 11px;
    letter-spacing: 2.2px;
    color: var(--brand-blue);
    font-weight: 700;
    white-space: nowrap;
  }
  .phone {
    position: absolute;
    left: 106px;
    top: 262px;
    display: flex;
    align-items: center;
    gap: 4px;
    color: var(--brand-green);
    font-size: 38px;
    font-weight: 700;
  }
  .phone svg { width: 42px; height: 48px; }
  .website {
    position: absolute;
    left: 18px;
    top: 318px;
    color: var(--brand-green);
    font-size: 37px;
    font-weight: 700;
    letter-spacing: -0.5px;
    white-space: nowrap;
  }
  .headline {
    position: absolute;
    left: 0;
    right: 0;
    top: 14px;
    text-align: center;
    color: var(--brand-blue);
    font-size: 30px;
    font-weight: 700;
    white-space: nowrap;
  }
  .staff {
    position: absolute;
    left: 18px;
    top: 70px;
    color: var(--ink-soft);
  }
  .staff__name { font-size: 20px; font-weight: 700; color: var(--brand-blue); }
  .staff__title { font-size: 14px; margin-top: 4px; }
  .events {
    position: absolute;
    left: 18px;
    top: 142px;
    list-style: none;
    padding: 0;
    color: var(--brand-green);
    font-size: 15px;
    font-weight: 700;
    line-height: 1.55;
  }
  .events__note { color: var(--ink-soft); font-weight: 400; font-style: normal; }
  .website--back {
    left: 16px;
    top: 326px;
    font-size: 18px;
    letter-spacing: 0;
  }
</style>
</head>
<body>
<main class="sheet">
  <section class="card card--front">
    <div class="card__photo" role="img" aria-label="Photo of two gold wedding rings on a wedding day invitation with a white ribbon"></div>
    <p class="brand brand--large"><span class="brand__dot"></span>Bright Lantern Sound</p>
    <p class="slogan-small">WE DO MORE THAN JUST PLAY MUSIC</p>
    <div class="phone">
      <svg viewBox="0 0 24 28" aria-hidden="true">
        <path d="M6 2c1.5-1 3 0 3.5 1.5l1.5 4c.4 1.2 0 2.2-1 2.8l-1.5 1c.8 3 2.5 5.5 4.8 7.3l1.6-.8c1-.5 2.1-.2 2.8.8l2.3 3.4c.8 1.3.4 2.8-.9 3.6-2 1.2-4.6 1.4-7-.2C7 21.5 3.4 15.8 3 10c-.2-3.4.9-6.6 3-8z" fill="currentColor"/>
      </svg>
      <span>415-762-9184</span>
    </div>
    <p class="website">www.brightlanternsound.com</p>
  </section>

  <section class="card card--back">
    <div class="card__photo" role="img" aria-label="Photo of two gold wedding rings on a wedding day invitation with a white ribbon"></div>
    <h1 class="headline">we do more than just play music</h1>
    <div class="staff">
      <p class="staff__name">Your Name Here</p>
      <p class="staff__title">Title</p>
    </div>
    <ul class="events">
      <li>Weddings, Anniversaries, Corporate Events</li>
      <li>Holiday Parties, Fund Raisers</li>
      <li class="events__note">or any event that needs entertainment</li>
    </ul>
    <p class="brand brand--small"><span class="brand__dot"></span>Bright Lantern Sound</p>
    <p class="website website--back">www.brightlanternsound.com</p>
  </section>
</main>
</body>
</html>
```